WALKING FOOD TOURISM BUSINESS. REQUEST FOR DIGITAL BROCHURE

Our business is a walking food tourism business in and around Melbourne's central city. We are needing a e-digital brochure - to be solely used as email' marketing content, not print. Therefore PDF size needs to be appropriate/suitable. Please see attached written content required for the brochure - together with our logo. For images, I am happy for designer to use our website content (www.wanderplatekitchen.com). OR any other appropriate and creative 'foodie' or Melbourne image suitable. Many thanks:)

Target Market(s)

Premium brand travellers or local adventurous Australians.

Requirements
Must have
• Quality font and images
Nice to have
• Quality Melbourne and food images. See website - wanderplatekitchen.com
Should not have
• Too much colour. Brand is black and white, sophisticated, premium product.

```html
<!DOCTYPE html>
<html lang="en">
<head>
<meta charset="utf-8">
<title>Our Experiences</title>
<link href="https://fonts.googleapis.com/css2?family=Source+Sans+3:wght@400;700&display=swap" rel="stylesheet">
<style>
  :root {
    --charcoal: #3a3a3a;
    --paper: #ffffff;
    --ink: #1f1f1f;
    --on-dark: #ffffff;
  }
  html, body {
    margin: 0;
    padding: 0;
    width: 1200px;
    height: 846px;
    overflow: hidden;
    background: var(--paper);
  }
  .brochure-page {
    position: relative;
    width: 1200px;
    height: 846px;
    overflow: hidden;
    font-family: "Source Sans 3", "Myriad Pro", Arial, sans-serif;
  }
  .backdrop {
    position: absolute;
    inset: 0;
    width: 1200px;
    height: 846px;
  }
  .page-title {
    position: absolute;
    left: 69px;
    top: 63px;
    margin: 0;
    font-size: 46px;
    line-height: 1;
    font-weight: 700;
    color: var(--on-dark);
    letter-spacing: -0.3px;
  }
  .experience {
    position: absolute;
    left: 69px;
    width: 680px;
  }
  .experience h2,
  .experience .experience-meta {
    margin: 0;
    font-size: 23px;
    line-height: 28px;
    font-weight: 700;
    letter-spacing: -0.1px;
  }
  .experience .experience-meta { margin-top: 7px; }
  .experience p.experience-copy {
    margin: 11px 0 0;
    font-size: 21px;
    line-height: 22.2px;
    font-weight: 400;
    letter-spacing: -0.2px;
  }
  .experience--city { top: 156px; color: var(--on-dark); }
  .experience--evening { top: 527px; color: var(--ink); }
  .photo {
    position: absolute;
    left: 792px;
    width: 356px;
    height: 264px;
  }
  .photo--drinks {
    top: 3px;
    background: linear-gradient(135deg, #8a6a4c 0%, #c9b79a 45%, #e4e0cf 60%, #7b5a3e 100%);
  }
  .photo--tarts {
    top: 292px;
    background: linear-gradient(120deg, #b58f6a 0%, #c0583a 35%, #f0d070 65%, #e9b95a 100%);
  }
  .photo--dish {
    top: 582px;
    background: radial-gradient(circle at 55% 55%, #e7a83a 0%, #e8d7b8 35%, #d8c6a6 70%, #6b5a48 100%);
  }
</style>
</head>
<body>
<main class="brochure-page">
  <svg class="backdrop" viewBox="0 0 1200 846" aria-hidden="true">
    <rect width="1200" height="846" fill="var(--paper)"/>
    <polygon points="0,0 1200,0 1200,396 0,518" fill="var(--charcoal)"/>
  </svg>

  <h1 class="page-title">Our Experiences</h1>

  <section class="experience experience--city">
    <h2>The Story of Melbourne</h2>
    <p class="experience-meta">2.5 hours / A$89 Adult / A$49 Child / Up to 12 guests</p>
    <p class="experience-copy">From the Yarra River to Iconic Laneways, Historic Precincts, Theatres<br>
    &amp; Cathedrals - discover the character, culture &amp; community of our<br>
    magnificent city, that is MELBOURNE.&nbsp; Walk with us on tour, as we share<br>
    stories about Melbourne’s past and present.&nbsp;&nbsp; Along your journey you’ll<br>
    take in the very fabric of Melbourne.&nbsp; From the early beginnings –<br>
    through to today, soaking in why Melbourne continues to be one of the<br>
    greatest multi-cultural cities in the world.</p>
  </section>

  <section class="experience experience--evening">
    <h2>Evening Palate &amp; Pairing</h2>
    <p class="experience-meta">3 hours / A$199 Adult / A$159 Child / Up to 8 guests</p>
    <p class="experience-copy">Enjoy your evening in one of Melbourne most vibrant,&nbsp; mouth-watering,<br>
    delectable foodie precincts.&nbsp; You’ll be ‘wowed’ by Melbourne’s charm<br>
    and hospitality as you experience signature tastes from some of our best<br>
    restaurants - pairing flavours and textures at each venue – and hearing<br>
    the stories that transformed Melbourne into the marvellous ‘food capital’<br>
    city it is today.</p>
  </section>

  <div class="photo photo--drinks" role="img" aria-label="Hands raising glasses of gin and tonic with lemon over a wooden table"></div>
  <div class="photo photo--tarts" role="img" aria-label="Trays of freshly baked custard tarts and nut tarts"></div>
  <div class="photo photo--dish" role="img" aria-label="Plated dish of fish with toasted corn and microgreens in a ceramic bowl"></div>
</main>
</body>
</html>
```